Valbrook Data Works

Our company is about IT hardwares and IT solutions. IT hardware such as PC, RAMS, storage and servers. IT solutions such as project management, BA. We are also selling new technology too.

Target Market(s)

Consumer, Small to Medium Business, Corporate

Requirements
Must have
• The business card must have the following:
• Name:
• Title:
• Contact Number:
• Email address:
• Website:
• Color: Must match the logo color upgrade

```html
<!DOCTYPE html>
<html lang="en">
<head>
<meta charset="utf-8">
<title>Valbrook Data Works – Business Card</title>
<link href="https://fonts.googleapis.com/css2?family=Lato:wght@400;700;900&display=swap" rel="stylesheet">
<style>
  :root {
    --bg: #2b2b2b;
    --ink: #1f1f1f;
    --ink-soft: #3a3a3a;
    --paper: #ffffff;
    --amber: #e0952f;
    --text: #222222;
  }
  * { margin: 0; padding: 0; box-sizing: border-box; }
  html, body { width: 1200px; height: 900px; overflow: hidden; }
  body {
    background: var(--bg);
    font-family: "Lato", Arial, sans-serif;
    position: relative;
  }
  .card {
    position: absolute;
    width: 540px;
    height: 310px;
    overflow: hidden;
  }
  .card-back {
    left: 80px; top: 80px;
    background: var(--ink);
    display: flex; flex-direction: column; align-items: center; justify-content: center;
  }
  .card-front {
    left: 580px; top: 510px;
    background: var(--paper);
  }
  .brand {
    display: flex; align-items: center; gap: 14px;
    font-weight: 900; font-size: 32px; letter-spacing: 0.5px;
    text-transform: uppercase; line-height: 1.05;
  }
  .brand-mark { width: 20px; height: 20px; background: var(--amber); flex: none; }
  .brand-name { max-width: 260px; }
  .card-back .brand-name { color: #ffffff; }
  .card-back .web {
    margin-top: 44px; color: #ffffff; font-size: 14px; letter-spacing: 0.5px;
  }
  .card-front .brand {
    position: absolute; left: 40px; top: 112px; font-size: 24px; gap: 10px;
  }
  .card-front .brand-mark { width: 14px; height: 14px; }
  .card-front .brand-name { color: var(--ink-soft); max-width: 190px; }
  .divider {
    position: absolute; left: 296px; top: 62px; width: 1px; height: 132px;
    background: var(--amber);
  }
  .contact {
    position: absolute; left: 318px; top: 28px; color: var(--text);
  }
  .contact .name { color: var(--amber); font-weight: 700; font-size: 21px; line-height: 1.2; }
  .contact .title { font-size: 13px; margin-top: 2px; }
  .contact .address { font-size: 13px; margin-top: 10px; line-height: 1.35; }
  .contact ul { list-style: none; margin-top: 8px; font-size: 13px; line-height: 1.6; }
  .contact li { display: flex; align-items: center; gap: 8px; }
  .contact li svg { width: 12px; height: 12px; fill: var(--amber); flex: none; }
  .wave { position: absolute; left: 0; top: 0; width: 540px; height: 310px; }
  .card-front .web {
    position: absolute; right: 22px; bottom: 20px; color: #ffffff; font-size: 13px;
  }
</style>
</head>
<body>

<section class="card card-back">
  <div class="brand"><span class="brand-mark"></span><span class="brand-name">Valbrook Data Works</span></div>
  <p class="web">www.valbrookdata.com</p>
</section>

<section class="card card-front">
  <svg class="wave" viewBox="0 0 540 310" aria-hidden="true">
    <path d="M0,310 L0,286 C180,282 360,252 540,218 L540,310 Z" fill="#1f1f1f"/>
    <path d="M130,278 C300,265 420,240 540,206 L540,213 C420,248 300,271 130,278 Z" fill="#e0952f"/>
    <path d="M100,274 C280,259 400,232 525,204 C400,238 280,266 100,274 Z" fill="#1f1f1f"/>
  </svg>

  <div class="brand"><span class="brand-mark"></span><span class="brand-name">Valbrook Data Works</span></div>

  <div class="divider"></div>

  <div class="contact">
    <p class="name">Daniel Hartwell</p>
    <p class="title">Manager</p>
    <p class="address">418 Alder Court<br>Houston, TX 77042</p>
    <ul>
      <li><svg viewBox="0 0 24 24"><path d="M6.6 10.8a15 15 0 0 0 6.6 6.6l2.2-2.2a1 1 0 0 1 1-.25 11.4 11.4 0 0 0 3.6.6 1 1 0 0 1 1 1V20a1 1 0 0 1-1 1A17 17 0 0 1 3 4a1 1 0 0 1 1-1h3.5a1 1 0 0 1 1 1c0 1.25.2 2.45.6 3.6a1 1 0 0 1-.25 1z"/></svg>512 555 0142</li>
      <li><svg viewBox="0 0 24 24"><path d="M6 2h12v6H6zM4 9h16a2 2 0 0 1 2 2v6h-4v5H6v-5H2v-6a2 2 0 0 1 2-2zm4 8v3h8v-3z"/></svg>512 555 0143</li>
      <li><svg viewBox="0 0 24 24"><path d="M2 5h20v14H2zm2 2v.5l8 5 8-5V7zm0 3v7h16v-7l-8 5z"/></svg>info@valbrookdata.com</li>
    </ul>
  </div>

  <p class="web">www.valbrookdata.com</p>
</section>

</body>
</html>
```